Need a new letterhead

Need a new fresh exciting letterhead. Remove the footer...info is outdated.

Target Market(s)

B2B

Industry/Entity Type

Electrical Power

Colors

Designer to choose colors to be used in the design.

Requirements
Must have
• Red and Blue Corvane Systems Logo
Nice to have
• Powering a cleaner, brighter grid in footer...reorganize the words?

```html
<!DOCTYPE html>
<html lang="en">
<head>
<meta charset="utf-8">
<title>Corvane Systems Letterhead</title>
<link href="https://fonts.googleapis.com/css2?family=Open+Sans:wght@400;700&family=Tinos&display=swap" rel="stylesheet">
<style>
  :root {
    --brand-red: #db1c24;
    --brand-blue: #34458f;
    --bar-blue: #243882;
    --ink: #555555;
    --backdrop: #e6e6e6;
  }
  * { margin: 0; padding: 0; box-sizing: border-box; }
  html, body { width: 1003px; height: 1200px; overflow: hidden; background: var(--backdrop); }
  .letterhead {
    position: absolute; left: 88px; top: 15px;
    width: 828px; height: 1170px;
    background: linear-gradient(180deg, #fafafa 0%, #f0f0f0 100%);
    box-shadow: 0 6px 24px rgba(0,0,0,0.18);
    overflow: hidden;
  }
  .brand-name {
    position: absolute; left: 97px; top: 66px;
    font-family: "Open Sans", sans-serif; font-weight: 700;
    font-size: 30px; line-height: 32px; color: var(--brand-red);
    display: flex; align-items: center; gap: 10px;
  }
  .brand-mark { width: 14px; height: 14px; background: var(--brand-red); flex: none; }
  .contact-panel {
    position: absolute; left: 482px; top: 63px; width: 346px; height: 82px;
    background: var(--brand-blue); color: #fff;
    font-family: "Open Sans", sans-serif; font-size: 11px; line-height: 13.7px;
    padding: 4px 96px 0 0; text-align: right;
  }
  .contact-line { display: flex; justify-content: flex-end; align-items: center; gap: 8px; white-space: nowrap; }
  .contact-line.iconed { margin-right: -14px; }
  .contact-line svg { width: 8px; height: 8px; flex: none; }
  .letter-body {
    position: absolute; left: 97px; top: 228px; width: 625px;
    font-family: "Tinos", "Times New Roman", serif; font-size: 17.5px; line-height: 20px;
    color: var(--ink);
  }
  .letter-body p { margin-bottom: 20px; }
  .recipient { margin-top: 39px; margin-bottom: 39px !important; }
  .recipient .indent { padding-left: 9px; }
  .closing { margin-top: 41px; }
  .signature { padding-left: 33px; }
  .gap-large { margin-bottom: 47px !important; }
  .tagline {
    position: absolute; left: 0; right: 0; top: 1104px; text-align: center;
    font-family: "Open Sans", sans-serif; font-size: 10px; letter-spacing: 5px;
    text-transform: uppercase; color: #444;
  }
  .tagline .initial { font-size: 14px; }
  .footer-bar { position: absolute; top: 1142px; height: 27px; }
  .footer-bar.red { left: 0; width: 475px; background: var(--brand-red); }
  .footer-bar.blue { left: 482px; width: 346px; background: var(--bar-blue); }
</style>
</head>
<body>
<div class="letterhead">
  <div class="brand-name"><span>Corvane<br>Systems</span><span class="brand-mark"></span></div>

  <div class="contact-panel">
    <div class="contact-line">18 Halden Street</div>
    <div class="contact-line">Marlow Heights, Ohio 44102</div>
    <div class="contact-line iconed">555-014-2260
      <svg viewBox="0 0 10 10"><path d="M2 1l2 2-1 1.5c.7 1.3 1.2 1.8 2.5 2.5L7 6l2 2-1.5 1.5C4 9 1 6 .5 2.5z" fill="#fff"/></svg></div>
    <div class="contact-line iconed">555-014-2261
      <svg viewBox="0 0 10 10"><rect x="2.5" y="0.5" width="5" height="3" fill="#fff"/><rect x="0.5" y="4" width="9" height="4" rx="1" fill="#fff"/></svg></div>
    <div class="contact-line iconed">www.corvanesystems.com
      <svg viewBox="0 0 10 10"><circle cx="5" cy="5" r="4.2" fill="none" stroke="#fff" stroke-width="1"/><path d="M1 5h8M5 1v8" stroke="#fff" stroke-width="0.8"/></svg></div>
  </div>

  <div class="letter-body">
    <p>Eastfield, NY 10988</p>
    <p>June 28, 2007</p>
    <p class="recipient">Ms. Dana Whitcombe<br>Alder Reed Fellowship<br><span class="indent">40 Linden Avenue</span><br>Westbrook, NY 10934</p>
    <p>Dear Ms. Whitcombe:</p>
    <p class="gap-large">The Alder Reed Fellowship has always loomed on the horizon for me. Ever since I decided to major in history, I have wanted to participate in your program. From the research that I have done, I believe that your program provides its participants with an extensively detailed look at the history of the world through hands-on experience with fossils, artifacts, and other remains that compose the blueprint of our existence.&nbsp; I am applying for the Alder Reed Fellowship because I believe that it would benefit me throughout my career and allow me to further understand the ideas behind history and how it is constructed.</p>
    <p>I believe my skills, experience, and goals make me an excellent candidate for your program.</p>
    <p>Thank you very much for considering me for the Alder Reed Fellowship. I am looking forward to hearing from you.</p>
    <p class="closing">Sincerely,</p>
    <p><span class="signature">Marin</span><br>(555) 017-3348</p>
  </div>

  <div class="tagline"><span class="initial">P</span>owering a cleaner, brighter grid</div>
  <div class="footer-bar red"></div>
  <div class="footer-bar blue"></div>
</div>
</body>
</html>
```